Deckblatt für Word-Vorlagen für Sachverständigen und Gutachter für stationäre Gaswarnanlagen
Zielgruppe
Ich bin Sachverständiger und Gutachter für stationäre Gaswarnanlagen. Dies kann man sich vorstellen wie eine Brandmeldeanlage nur für Gase, also Bereich Mess- und Regeltechnik gemischt mit Sicherheitstechnik und dies rein als Sachverständiger.
Meine Zielgruppe sind rein nur Firmen und davon meistens Großkonzerne. Mein Erscheinungsbild muss als Wertig, Seriös und Teuer sein.
Aufgabenstellung
Ich benötige nur ein neues Deckblatt für Word-Vorlagen.
Das Deckblatt ist rein für meine Gutachten und Beurteilungen, sollte also nicht 'verspielt' sein.
Anbei die alte Version mit einer Office Vorlage und den Daten welche ich immer eintragen muss. Zusätzlich anbei meine neue Power Point Masterfolien-Vorlage, rein als Info. Das Deckblatt, wie auch alle späteren Seiten, sollen das Wasserzeichen (rundes Logo) behalten.

```html
<!DOCTYPE html>
<html lang="de">
<head>
<meta charset="utf-8">
<title>Gutachten Deckblatt – Gasprüf-Kontor</title>
<link href="https://fonts.googleapis.com/css2?family=Noto+Sans:wght@400;700&display=swap" rel="stylesheet">
<style>
  :root {
    --page-bg: #ffffff;
    --stage-bg: #ecedf0;
    --brand-blue: #4a64a3;
    --ink: #3b3b3b;
    --ink-soft: #555a60;
    --accent-yellow: #f2c12e;
    --watermark: #e9ecf3;
    --badge-ring: #c9ccd2;
  }
  * { margin: 0; padding: 0; box-sizing: border-box; }
  html, body { width: 811px; height: 1200px; overflow: hidden; background: var(--stage-bg); }
  .cover {
    position: relative; width: 811px; height: 1200px; overflow: hidden;
    background: var(--page-bg);
    font-family: "Noto Sans", Verdana, sans-serif; color: var(--ink);
  }
  .brand { position: absolute; left: 48px; top: 72px; }
  .brand-name { display: block; font-size: 34px; font-weight: 700; color: var(--ink); line-height: 1.1; }
  .brand-descriptor { display: block; margin-top: 6px; font-size: 14px; font-weight: 400; color: var(--ink-soft); }

  .report-title { position: absolute; left: 48px; top: 200px; font-size: 44px; font-weight: 700; line-height: 1.18; color: var(--ink); }
  .report-title .highlight { color: var(--brand-blue); }

  .expert { position: absolute; left: 48px; top: 330px; padding-left: 18px; border-left: 4px solid var(--accent-yellow); font-size: 15px; line-height: 1.45; color: var(--ink-soft); }
  .expert-name { color: var(--brand-blue); font-weight: 700; font-size: 16px; }

  .details { position: absolute; left: 500px; top: 445px; width: 280px; font-size: 13.5px; line-height: 1.55; color: var(--ink-soft); }
  .detail-block { position: relative; padding-left: 38px; margin-bottom: 22px; }
  .detail-block::before { content: ""; position: absolute; left: 0; top: 10px; width: 28px; height: 3px; background: var(--accent-yellow); }
  .detail-label { color: var(--brand-blue); font-weight: 700; }

  .watermark { position: absolute; left: 40px; top: 640px; width: 520px; height: 520px; border-radius: 50%;
    background: radial-gradient(circle at 45% 40%, #f3f5f9 0%, var(--watermark) 70%, #e2e6ef 100%); }

  .report-number { position: absolute; left: 48px; top: 985px; font-size: 19px; color: var(--ink-soft); }

  .footer-band { position: absolute; left: 0; bottom: 0; width: 811px; height: 190px; }
  .footer-contact { position: absolute; bottom: 48px; font-size: 17px; line-height: 1.55; color: #e6ebf6; }
  .footer-address { left: 48px; }
  .footer-reach { left: 380px; }

  .seal { position: absolute; left: 640px; top: 915px; width: 118px; height: 118px; border-radius: 50%;
    background: #fff; border: 6px solid var(--badge-ring); box-shadow: 0 0 0 3px #fff; }
</style>
</head>
<body>
<main class="cover">
  <div class="watermark" role="img" aria-label="Großes, blasses rundes Wasserzeichen"></div>

  <header class="brand">
    <span class="brand-name">Gasprüf-Kontor</span>
    <span class="brand-descriptor">Sachverständigenbüro für stationäre Gaswarnanlagen</span>
  </header>

  <h1 class="report-title">Ihr Berichtstitel wird<br><span class="highlight">hier eingetragen</span></h1>

  <section class="expert">
    <div class="expert-name">Lorenz Varnhold</div>
    <div>Geprüfter Sachverständiger für Gaswarntechnik</div>
    <div>Fachkraft für Explosionsschutz</div>
  </section>

  <section class="details">
    <div class="detail-block">
      <div class="detail-label">Auftraggeber</div>
      <div>Agrarhandel Mittelrhein eG</div>
      <div>Kaiwall 7 D-50321 Brühlhausen</div>
    </div>
    <div class="detail-block">
      <div class="detail-label">Standort</div>
      <div>Pflanzenschutzmittellager</div>
      <div>Hafenweg 22</div>
      <div>D-41812 Erkenrath</div>
    </div>
  </section>

  <p class="report-number">Gutachten-Nr. 1202/001-01 vom 19 Januar 2021</p>

  <svg class="footer-band" viewBox="0 0 811 190" aria-hidden="true">
    <path d="M0 50 H560 Q580 50 590 40 L620 10 Q630 0 650 0 H811 V190 H0 Z" fill="var(--brand-blue)"/>
  </svg>
  <div class="footer-contact footer-address">Lindenhof 4<br>D-35418 Burgwetten</div>
  <div class="footer-contact footer-reach">Tel. 06031/48215-0<br>kontakt@gaspruef-kontor.de</div>

  <div class="seal" role="img" aria-label="Siegel eines Sachverständigenverbands"></div>
</main>
</body>
</html>
```